Existing Website Requiring new Pages

I have an existing word press website that was built using elementor.
Website: www.tallowmerecare.com.au
I require the Vacancies page (https://www.tallowmerecare.com.au/vacancies/) to be modified to display our new properties along with minor tweaks to how the information is presented.
The vacancies to be displayed are the exactly the same as those that are located on the homepage of QDA website (https://qda.org.au/)
The new pages that link off the Vacancies tab will require custom design.
There are roughly 8 pages/properties to be incorporated. i wish for the design to be very similar to that displayed in the following link; https://www.zomplex.com.au/vacancies/merrylands
Along with this the back end has not been updated for the last 3 years so it also requires some maintenance.
Website is in the disability industry and the custom pages will display information relative to Property Vacancies.
I have attached a ZIP file with some design guides, the information for each of the properties (which will need to be modified to show our business name Tallowmere Healthcare) and the example of how it is to look based off the Zomplex website.
If you guys have any suggestions or ideas on how to make this more presentable or possible i'm open to your ideas.
People looking for SDA properties custom built for people with a disability
Disability
Coded - Design and coding required
5+ page

```html
<!DOCTYPE html>
<html lang="en">
<head>
<meta charset="utf-8">
<title>Vacancies – Tallowmere Healthcare</title>
<link rel="stylesheet" href="https://fonts.googleapis.com/css2?family=Rubik:wght@400;500;700;900&family=Roboto:wght@400;500;700&family=Montserrat:wght@400;500&display=swap">
<style>
:root{
  --teal:#2ecbb4;
  --teal-dark:#22b8a2;
  --orange:#fb8c4f;
  --purple:#7b5bd0;
  --blue:#1aa3e0;
  --ink:#222;
  --muted:#555;
  --card:#f5f5f5;
  --footer:#f7f7f7;
  --bar:#232323;
  --white:#fff;
}
*{box-sizing:border-box;margin:0;padding:0}
html,body{width:1200px;height:3169px;overflow:hidden}
body{font-family:Roboto,Arial,sans-serif;color:var(--ink);background:var(--white);position:relative}
.wrap{position:absolute;left:138px;width:927px}

/* header */
.site-header{position:absolute;top:0;left:0;width:1200px;height:103px;background:var(--white)}
.brand{position:absolute;left:138px;top:30px;display:flex;align-items:center;gap:8px;font-family:Rubik,sans-serif;font-weight:500;font-size:17px;color:var(--purple);line-height:1.05}
.brand-dot{width:26px;height:26px;border-radius:50%;background:var(--teal)}
.main-nav{position:absolute;right:135px;top:45px;display:flex;gap:23px;font-family:Roboto,sans-serif;font-weight:700;font-size:10.5px;letter-spacing:.6px;color:#333}
.main-nav .active{color:var(--orange)}

/* hero */
.hero{position:absolute;top:103px;left:0;width:1200px;height:514px}
.hero-panel{position:absolute;left:0;top:0;width:587px;height:514px;background:var(--teal)}
.hero-photo{position:absolute;left:587px;top:0;width:613px;height:514px;background:linear-gradient(160deg,#9bb8cf 0%,#c6d6e2 40%,#5f6e7c 100%)}
.hero-title{position:absolute;left:138px;top:126px;font-family:Rubik,sans-serif;font-weight:900;font-size:58px;color:var(--white);letter-spacing:.5px}
.hero-text{position:absolute;left:138px;top:193px;width:390px;font-size:12.2px;line-height:20px;color:var(--white)}
.btn-contact{position:absolute;left:138px;top:300px;width:163px;height:50px;border-radius:25px;background:var(--white);color:var(--teal);font-family:Roboto,sans-serif;font-weight:500;font-size:15px;display:flex;align-items:center;justify-content:center;gap:6px}

/* search */
.search{position:absolute;left:138px;top:535px;width:927px;height:155px;border-radius:78px;background:var(--orange)}
.field{position:absolute;top:45px;width:213px}
.field label{display:block;font-family:Roboto,sans-serif;font-weight:500;font-size:12.5px;color:var(--white);margin-bottom:8px}
.select{height:42px;background:var(--white);border-radius:2px;display:flex;align-items:center;justify-content:space-between;padding:0 12px 0 18px;font-size:12px;color:#555}
.select::after{content:"";border-left:5px solid transparent;border-right:5px solid transparent;border-top:5px solid #777}
.btn-search{position:absolute;left:739px;top:70px;width:130px;height:42px;border-radius:3px;background:var(--purple);color:var(--white);font-family:Rubik,sans-serif;font-weight:700;font-size:15px;display:flex;align-items:center;justify-content:center}

/* properties */
.section-kicker{position:absolute;top:736px;width:1200px;text-align:center;font-family:Rubik,sans-serif;font-weight:500;font-size:23px;color:var(--purple)}
.section-title{position:absolute;top:767px;width:1200px;text-align:center;font-family:Rubik,sans-serif;font-weight:700;font-size:26px;color:var(--ink)}
.map{position:absolute;left:138px;top:826px;width:927px;height:429px;background:linear-gradient(100deg,#dbe9dd 0%,#c9e3cc 45%,#e9efe9 70%,#cfe6f3 100%)}

.cards{position:absolute;left:138px;top:1291px;width:927px;display:grid;grid-template-columns:repeat(3,299px);column-gap:15px;row-gap:18px}
.card{height:384px;background:var(--card);position:relative}
.card-photo{height:250px;position:relative;background:linear-gradient(180deg,#a9cdef 0%,#d5e3ee 45%,#a88a70 62%,#6f9a4f 100%)}
.badge{position:absolute;top:15px;height:14px;padding:0 5px;font-family:Roboto,sans-serif;font-weight:700;font-size:7.5px;color:var(--white);display:flex;align-items:center;letter-spacing:.2px}
.badge.featured{left:12px;background:var(--purple)}
.badge.now{right:107px;background:var(--teal)}
.badge.vacancy{right:11px;background:var(--blue)}
.card-body{padding:19px 23px 0}
.card-title{font-family:Rubik,sans-serif;font-weight:500;font-size:18px;color:#222}
.card-sub{font-size:10.5px;color:#444;margin-top:5px}
.card-text{font-size:10.5px;color:#444;margin-top:8px}
.btn-details{margin-top:10px;width:94px;height:32px;border-radius:2px;background:var(--orange);color:var(--white);font-family:Roboto,sans-serif;font-weight:700;font-size:11px;display:flex;align-items:center;justify-content:center;letter-spacing:.4px}

.btn-load{position:absolute;left:499px;top:2116px;width:214px;height:62px;border-radius:31px;background:var(--teal);color:var(--white);font-family:Rubik,sans-serif;font-weight:500;font-size:18px;display:flex;align-items:center;justify-content:center;gap:12px}

.video-title{position:absolute;top:2232px;width:1200px;text-align:center;font-family:Rubik,sans-serif;font-weight:700;font-size:33px;color:var(--purple)}
.video{position:absolute;left:138px;top:2299px;width:927px;height:459px;background:linear-gradient(180deg,#7fb6ea 0%,#c5a58b 35%,#a9734f 55%,#4f7c2d 78%,#6ea33a 100%)}
.play{position:absolute;left:431px;top:197px}

/* footer */
.site-footer{position:absolute;top:2844px;left:0;width:1200px;height:267px;background:var(--footer)}
.footer-brand{position:absolute;left:150px;top:110px;display:flex;align-items:center;gap:8px;font-family:Montserrat,sans-serif;font-weight:500;font-size:17px;color:var(--purple);line-height:1.1}
.footer-contact{position:absolute;left:150px;top:186px;font-family:Montserrat,sans-serif;font-size:11.5px;line-height:20px;color:var(--purple)}
.footer-contact li{list-style:none;display:flex;align-items:center;gap:8px}
.footer-social{position:absolute;left:529px;top:60px;display:flex;flex-direction:column;gap:10px}
.footer-social span{width:28px;height:28px;border-radius:50%;background:#2b2b6b;display:block}
.footer-social span:first-child{background:#7b3b8f}
.footer-social span:nth-child(2){background:#2c5faa}
.footer-social span:nth-child(3){background:#222}
.footer-social span:nth-child(4){background:#1d6fb0}
.footer-col{position:absolute;top:64px;width:210px;font-family:Montserrat,sans-serif}
.footer-col h4{font-weight:500;font-size:12.5px;color:#333;border-left:3px solid var(--blue);padding-left:10px;margin-bottom:10px;letter-spacing:.3px}
.footer-col li{list-style:none;font-size:11px;line-height:20px;color:#888;border-bottom:1px solid #e6e6e6;padding:5px 0}
.footer-bar{position:absolute;top:3111px;left:0;width:1200px;height:58px;background:var(--bar);color:#bbb;font-size:9px;display:flex;align-items:center;justify-content:center}
</style>
</head>
<body>

<header class="site-header">
  <div class="brand"><span class="brand-dot"></span><span>Tallowmere<br>Healthcare</span></div>
  <nav class="main-nav">
    <span>HOME</span><span>ABOUT US</span><span class="active">WHAT WE DO ▾</span><span>REFERRALS</span><span>FEEDBACK</span><span>CONTACT US</span>
  </nav>
</header>

<section class="hero">
  <div class="hero-panel"></div>
  <div class="hero-photo" role="img" aria-label="Smiling woman in a wheelchair working on a laptop outside a glass office building"></div>
  <h1 class="hero-title">VACANCIES</h1>
  <p class="hero-text">Lorem Ipsum is simply dummy text of the printing and typesetting industry. Lorem Ipsum has been the industry's standard dummy text ever since the industry, when an unknown printer took best gallery type and scrambled it to make a type specimen book.</p>
  <a class="btn-contact">
    <svg width="15" height="12" viewBox="0 0 15 12"><rect x="1" y="1" width="13" height="10" rx="1" fill="none" stroke="currentColor" stroke-width="1.5"/><path d="M1.5 1.5 7.5 6.5 13.5 1.5" fill="none" stroke="currentColor" stroke-width="1.5"/></svg>
    CONTACT US
  </a>
</section>

<form class="search">
  <div class="field" style="left:64px"><label>CURRENT OR FUTURE</label><div class="select">Both</div></div>
  <div class="field" style="left:290px"><label>DESIGN CATEGORY</label><div class="select">All Categories</div></div>
  <div class="field" style="left:515px"><label>LOCATION</label><div class="select">All Suburbs</div></div>
  <div class="btn-search">SEARCH</div>
</form>

<p class="section-kicker">PROPERTIES</p>
<h2 class="section-title">VIEW OUR SDA VACANCIES AND HOMES BEING BUILT</h2>
<div class="map" role="img" aria-label="Map of western Sydney and the Blue Mountains with property location markers"></div>

<div class="cards">
  <article class="card"><div class="card-photo" role="img" aria-label="Brick house with garage and hedges"><span class="badge featured">FEATURED</span><span class="badge now">AVAILABLE NOW</span><span class="badge vacancy">CURRENT VACANCY</span></div>
    <div class="card-body"><h3 class="card-title">Penrith</h3><p class="card-sub">4 Bedroom SIL Home</p><p class="card-text">Lorem Ipsum is simply dummy text of the printing</p><div class="btn-details">DETAILS</div></div></article>
  <article class="card"><div class="card-photo" role="img" aria-label="Red brick house with paved driveway"><span class="badge featured">FEATURED</span><span class="badge now">AVAILABLE NOW</span><span class="badge vacancy">CURRENT VACANCY</span></div>
    <div class="card-body"><h3 class="card-title">Mount Druitt</h3><p class="card-sub">4 Bedroom SIL Home</p><p class="card-text">Lorem Ipsum is simply dummy text of the printing</p><div class="btn-details">DETAILS</div></div></article>
  <article class="card"><div class="card-photo" role="img" aria-label="Cream rendered house with dark roof"><span class="badge featured">FEATURED</span><span class="badge now">AVAILABLE NOW</span><span class="badge vacancy">CURRENT VACANCY</span></div>
    <div class="card-body"><h3 class="card-title">Casula</h3><p class="card-sub">4 Bedroom SIL Home</p><p class="card-text">Lorem Ipsum is simply dummy text of the printing</p><div class="btn-details">DETAILS</div></div></article>
  <article class="card"><div class="card-photo" role="img" aria-label="Federation style brick house with front path"><span class="badge featured">FEATURED</span><span class="badge now">AVAILABLE NOW</span><span class="badge vacancy">CURRENT VACANCY</span></div>
    <div class="card-body"><h3 class="card-title">Eastwood</h3><p class="card-sub">4 Bedroom SIL Home</p><p class="card-text">Lorem Ipsum is simply dummy text of the printing</p><div class="btn-details">DETAILS</div></div></article>
  <article class="card"><div class="card-photo" role="img" aria-label="House with palm tree and double garage"><span class="badge featured">FEATURED</span><span class="badge now">AVAILABLE NOW</span><span class="badge vacancy">CURRENT VACANCY</span></div>
    <div class="card-body"><h3 class="card-title">Baulkham Hills</h3><p class="card-sub">4 Bedroom SIL Home</p><p class="card-text">Lorem Ipsum is simply dummy text of the printing</p><div class="btn-details">DETAILS</div></div></article>
  <article class="card"><div class="card-photo" role="img" aria-label="Orange brick house with long driveway"><span class="badge featured">FEATURED</span><span class="badge now">AVAILABLE NOW</span><span class="badge vacancy">CURRENT VACANCY</span></div>
    <div class="card-body"><h3 class="card-title">Merrylands</h3><p class="card-sub">4 Bedroom SIL Home</p><p class="card-text">Lorem Ipsum is simply dummy text of the printing</p><div class="btn-details">DETAILS</div></div></article>
</div>

<div class="btn-load">LOAD MORE
  <svg width="34" height="34" viewBox="0 0 34 34" fill="none" stroke="#fff" stroke-width="2.5" stroke-linecap="round">
    <path d="M17 3v6M17 25v6M3 17h6M25 17h6M7 7l4 4M23 23l4 4M27 7l-4 4M11 23l-4 4"/>
  </svg>
</div>

<h2 class="video-title">WATCH OUR VIDEO</h2>
<div class="video" role="img" aria-label="Video thumbnail of a brick home with red tiled roof, hedge and paved driveway">
  <svg class="play" width="66" height="66" viewBox="0 0 66 66"><circle cx="33" cy="33" r="33" fill="rgba(0,0,0,.6)"/><path d="M26 20 48 33 26 46Z" fill="#fff"/></svg>
</div>

<footer class="site-footer">
  <div class="footer-brand"><span class="brand-dot"></span><span>Tallowmere<br>Healthcare</span></div>
  <ul class="footer-contact">
    <li><svg width="12" height="10" viewBox="0 0 12 10"><rect x=".75" y=".75" width="10.5" height="8.5" fill="none" stroke="#e0459b" stroke-width="1.3"/><path d="M1 1l5 4 5-4" fill="none" stroke="#e0459b" stroke-width="1.3"/></svg>Email: info@tallowmerecare.com.au</li>
    <li><svg width="12" height="12" viewBox="0 0 12 12"><path d="M2 1h3l1 3-2 1a7 7 0 0 0 3 3l1-2 3 1v3c-6 0-10-4-9-9Z" fill="#e0459b"/></svg>Phone: +61 0491 570 156</li>
    <li><svg width="12" height="12" viewBox="0 0 12 12"><circle cx="6" cy="6" r="5" fill="none" stroke="#e0459b" stroke-width="1.3"/><path d="M6 3v3l2 1" fill="none" stroke="#e0459b" stroke-width="1.3"/></svg>Operating Hours: 9AM To 5PM Monday - Friday</li>
  </ul>
  <div class="footer-social"><span></span><span></span><span></span><span></span></div>
  <div class="footer-col" style="left:614px"><h4>ACCOMMODATION</h4><ul>
    <li>Supported Independent Living (SIL)</li><li>Specialist Disability Accommodation (SDA)</li><li>Short term Accommodation (Respite)</li><li>Vacancies</li></ul></div>
  <div class="footer-col" style="left:846px"><h4>WHAT WE DO</h4><ul>
    <li>In Home Care</li><li>Social &amp; Community Services</li><li>Therapeutic Supports</li><li>Support Coordination</li><li>Home Modifications</li></ul></div>
</footer>
<div class="footer-bar">© Copyright 2021 | Tallowmere Healthcare | All Rights Reserved.</div>

</body>
</html>
```